Design & Content Treatments for small Tai Chi Teacher's Site

Wordpress is setup and ready to go. Really just need a header image (with text treatment of the site name and tag line), and really simple content treatments for each page (image selection and placement, etc). Ideally this will require very little modification to the actual wordpress template code.
Simpler is better. I will post images and am in the process of flowing all the text into the site now. If some sort of Iconic identity can be established Marek will be VERY happy, but it's not a requirement
Thank You!
Temporary Site URL is http://203.0.113.58/~cedarlx4/
Final will be cedarlanternmovement.com.

```html
<!DOCTYPE html>
<html lang="en">
<head>
<meta charset="utf-8">
<title>Cedar Lantern T'ai Chi</title>
<link rel="stylesheet" href="https://fonts.googleapis.com/css2?family=Didact+Gothic&family=Questrial&display=swap">
<style>
  :root{
    --page-bg-top:#2e3436;
    --page-bg-bottom:#b7c2cc;
    --sheet:#efeff7;
    --ink:#4a4a4a;
    --ink-soft:#666;
    --title:#333;
    --nav-top:#7d8386;
    --nav-bottom:#45494b;
    --nav-text:#f2f2f2;
    --frame:#b9c3c8;
    --photo-light:#5e96cf;
    --photo-deep:#2b62a6;
    --portrait-light:#8a9188;
    --portrait-deep:#4a4f4c;
    --side-top:#dfe4e8;
    --side-bottom:#d7dde1;
  }
  *{box-sizing:border-box;margin:0;padding:0}
  html,body{width:1200px;height:1150px;overflow:hidden}
  body{
    position:relative;
    background:linear-gradient(180deg,var(--page-bg-top) 0,#6f7a80 35%,var(--page-bg-bottom) 100%);
    font-family:"Didact Gothic",sans-serif;
    color:var(--ink);
  }
  .sheet{position:absolute;left:113px;top:0;width:974px;height:1118px;background:var(--sheet)}
  .masthead{
    position:absolute;left:0;top:0;width:974px;height:127px;
    background:radial-gradient(ellipse 420px 110px at 780px 60px,#ffffff 0,rgba(255,255,255,0) 70%),
               linear-gradient(90deg,var(--sheet) 30%,#dfe3ea 70%,#c9d0d8 100%);
  }
  .brand-dot{position:absolute;left:40px;top:6px;width:115px;height:115px;border-radius:50%;background:#8e9498}
  .brand-name{position:absolute;left:164px;top:39px;font-family:"Questrial",sans-serif;font-size:24px;font-weight:700;color:var(--title);letter-spacing:.3px}
  .tagline{position:absolute;left:164px;top:72px;font-family:"Questrial",sans-serif;font-size:14.5px;font-weight:700;color:var(--title);letter-spacing:.3px}
  .main-nav{
    position:absolute;left:30px;top:127px;width:914px;height:35px;
    background:linear-gradient(180deg,var(--nav-top),var(--nav-bottom));
    display:flex;align-items:center;
  }
  .main-nav::after{content:"";position:absolute;left:0;top:35px;width:914px;height:16px;background:linear-gradient(180deg,#c4c9cc,#eceef2)}
  .nav-item{color:var(--nav-text);font-size:13px;display:flex;align-items:center;white-space:nowrap;margin-top:-2px}
  .hero{position:absolute;left:30px;top:194px;width:721px;height:268px;border:6px solid var(--frame);background:#fff}
  .hero-photo{width:709px;height:256px;background:linear-gradient(180deg,var(--photo-light),var(--photo-deep))}
  .profile{position:absolute;left:758px;top:194px;width:182px;height:268px;border:5px solid var(--frame);background:#fff}
  .profile h3{font-weight:400;font-size:13px;color:var(--ink-soft);margin:7px 0 0 6px;display:flex;align-items:center;gap:6px;letter-spacing:.3px}
  .profile-photo{position:absolute;left:8px;top:32px;width:158px;height:221px;border:1px solid #bbb;padding:4px}
  .profile-photo div{width:100%;height:100%;background:linear-gradient(180deg,var(--portrait-light),var(--portrait-deep))}
  .content{position:absolute;left:32px;top:476px;font-size:11.5px;line-height:15.3px;letter-spacing:.7px}
  .content h1{font-weight:400;font-size:16px;color:var(--ink-soft);margin-bottom:17px;letter-spacing:.2px}
  .content p{width:672px;margin-bottom:15px}
  .benefits{list-style:none;margin-top:22px}
  .benefits li{position:relative;width:660px;padding-left:12px;margin-bottom:20px}
  .benefits li::before{content:"";position:absolute;left:0;top:5px;width:4px;height:4px;background:#777}
  .benefits li.spaced{margin-bottom:25px}
  .benefits li.wide{width:912px;margin-bottom:15px}
  .content p.wide{width:912px;letter-spacing:.55px}
  .sidebar{position:absolute;left:720px;top:483px;width:224px;height:401px;border-radius:8px;
    background:linear-gradient(180deg,var(--side-top),#f4f6f8 45%,#eef1f3 75%,var(--side-bottom))}
  .search{position:absolute;left:13px;top:22px;width:155px;height:21px;background:linear-gradient(90deg,#ccc,#fff 12%,#fff 85%,#ccc)}
  .search-btn{position:absolute;left:170px;top:22px;width:40px;height:22px;background:#111;color:#fff;font-size:11px;text-align:center;line-height:21px;border-radius:2px}
  .widget-title{position:absolute;left:8px;font-weight:400;font-size:14px;color:var(--ink-soft);display:flex;align-items:center;gap:12px;letter-spacing:.4px}
  .calendar{position:absolute;left:12px;top:100px;font-size:10.5px;color:#555;border-collapse:collapse;letter-spacing:.3px}
  .calendar td,.calendar th{font-weight:400;width:16px;height:15px;text-align:center;padding:0}
  .blog-list{position:absolute;left:10px;top:262px;list-style:none;font-size:11.5px;color:#555;letter-spacing:.5px}
  .blog-list li{position:relative;padding-left:21px;margin-bottom:6px}
  .blog-list li::before{content:"";position:absolute;left:0;top:6px;width:4px;height:4px;background:#888}
  .footer{position:absolute;left:0;top:1129px;width:1200px;text-align:center;font-size:11.5px;color:#3a3f44;letter-spacing:.5px}
</style>
</head>
<body>
<div class="sheet">
  <header class="masthead">
    <div class="brand-dot"></div>
    <div class="brand-name">Cedar Lantern T'ai Chi</div>
    <div class="tagline">Group and Private T'ai Chi Ch'uan Instruction by Marek Dunford</div>
  </header>

  <nav class="main-nav">
    <span class="nav-item" style="margin-left:19px">Welcome<svg width="60" height="8"><path d="M33 2h6l-3 4z" fill="#eee"/></svg></span>
    <span class="nav-item" style="margin-left:4px">Schedule<svg width="48" height="8"><path d="M21 2h6l-3 4z" fill="#eee"/></svg></span>
    <span class="nav-item" style="margin-left:11px">Class Types<svg width="60" height="8"><path d="M22 2h6l-3 4z" fill="#eee"/></svg></span>
    <span class="nav-item" style="margin-left:-8px">About T'ai Chi<svg width="50" height="8"><path d="M21 2h6l-3 4z" fill="#eee"/></svg></span>
    <span class="nav-item" style="margin-left:1px">Mentorship and Life Guidance<svg width="58" height="8"><path d="M21 2h6l-3 4z" fill="#eee"/></svg></span>
    <span class="nav-item" style="margin-left:-8px">Blog<svg width="54" height="8"><path d="M23 2h6l-3 4z" fill="#eee"/></svg></span>
    <span class="nav-item" style="margin-left:2px">Contact Marek</span>
  </nav>

  <div class="hero"><div class="hero-photo" role="img" aria-label="Banner photograph: rocky green islands rising from deep blue sea under a clear sky"></div></div>

  <aside class="profile">
    <h3><svg width="12" height="8"><path d="M0 4h9M6 1l3 3-3 3" stroke="#888" stroke-width="1.5" fill="none"/></svg>Marek Dunford</h3>
    <div class="profile-photo"><div role="img" aria-label="Portrait photo of the instructor outdoors"></div></div>
  </aside>

  <main class="content">
    <h1>Welcome to Cedar Lantern T'ai Chi</h1>
    <p>I am dedicated to sharing the profound and limitless potential of t'ai chi ch'uan as a method for self-healing – for achieving balance in all areas of life – and for the recovery of the optimum health and the integration of the body, mind and spirit.</p>
    <p>Inherent within t'ai chi, of course is it's martial function and it's potential for self-defense has been well documented and elucidated by numerous masters and adepts alike. Thus I will not treat the subject here, beyond to say that with daily practice over a period of time one will assuredly be able to defend oneself without a doubt.</p>
    <p>Some of the many benefits of a sincere and diligent t'ai chi ch'uan practice include but are not limited to:</p>
    <ul class="benefits">
      <li>The facilitation of stress release and the unwinding of tension in the body leading to the dissolution of blockages, vitalizing the energy meridians and enhanced energy flow to all areas of the body.</li>
      <li>Through the rhythmic movement of t'ai chi the internal organs are gently massaged and tonified, leading to their optimum healthy function.</li>
      <li class="spaced">The central nervous system is likewise strengthened, developed and refined through regular t'ai chi practice.</li>
      <li class="spaced">The facilitation of a balanced emotional body, leading to their healthy and appropriate expression.</li>
      <li>The peaceful mental atmosphere facilitated by t'ai chi movement allows negative thought patterns to dissolve and be replaced by positive, life enforcing attitudes.</li>
      <li>Experience real personal development and a renewed sense of purpose through the embodiment of universal principles inherent within you and vitalized or actualized through your sincere t'ai chi ch'uan practice.</li>
      <li class="wide">With regular t'ai chi practice, one may discover that there is less need for sleep and substantially more energy available for attending to the many activities and responsibilities in daily life.</li>
    </ul>
    <p class="wide">Though all are encouraged to experience the healing, harmonizing and self-developing characteristics of t'ai chi, there are those who may prefer another way. For these individuals there are various study groups, Constructive Life Guidance and Resonance Healing treatments offered. Practically speaking, there are many practices or methods for achieving the recovery of ones self-nature. For more information about these, and other services please click on the Life Guidance and Class Description tabs, or feel free to contact me for a complimentary initial consultation either on the phone or in person.</p>
    <p style="margin-top:20px">Sincerely,<br>Marek Dunford</p>
  </main>

  <aside class="sidebar">
    <div class="search"></div>
    <div class="search-btn">search</div>
    <h3 class="widget-title" style="top:68px"><svg width="12" height="8"><path d="M0 4h9M6 1l3 3-3 3" stroke="#888" stroke-width="1.5" fill="none"/></svg>Upcoming Classes</h3>
    <table class="calendar">
      <tr><td colspan="7" style="text-align:left;padding-left:5px">&lt;&lt;&nbsp;&nbsp; Sep 2011 &nbsp;&nbsp;&gt;&gt;</td></tr>
      <tr><th>S</th><th>M</th><th>T</th><th>W</th><th>T</th><th>F</th><th>S</th></tr>
      <tr><td>28</td><td>29</td><td>30</td><td>31</td><td>1</td><td>2</td><td>3</td></tr>
      <tr><td>4</td><td>5</td><td>6</td><td>7</td><td>8</td><td>9</td><td>10</td></tr>
      <tr><td>11</td><td>12</td><td>13</td><td>14</td><td>15</td><td>16</td><td>17</td></tr>
      <tr><td>18</td><td>19</td><td>20</td><td>21</td><td>22</td><td>23</td><td>24</td></tr>
      <tr><td>25</td><td>26</td><td>27</td><td>28</td><td>29</td><td>30</td><td>1</td></tr>
    </table>
    <h3 class="widget-title" style="top:234px"><svg width="12" height="8"><path d="M0 4h9M6 1l3 3-3 3" stroke="#888" stroke-width="1.5" fill="none"/></svg>Recent Blog Posts</h3>
    <ul class="blog-list">
      <li>173</li>
      <li>Lipsum</li>
      <li>Hello world!</li>
    </ul>
  </aside>
</div>
<footer class="footer">© copyright by Cedar Lantern T'ai Chi. 2011 All Rights Reserved</footer>
</body>
</html>
```